Local Flower Farm Needs Business Card Design

I need business cards designed for a flower farm based in Eudora, Kansas.
Business Info:
We are a local cut flower farm located in Eudora, Kansas, founded by Darla Hoffstrom. What started as a passion for agriculture and search for more joy in daily life has blossomed into a small business dedicated to providing the community with beautiful, fresh, and sustainable flowers. We specialize in local, seasonal blooms, ensuring that every petal reflects the care and dedication we pour into our craft. Our mission is to deliver the highest quality flowers directly to our customers through local farmers markets and to florists who share our commitment to sustainability. Join us in celebrating the beauty of nature, one bloom at a time!
Contact Details:
Darla Hoffstrom
Owner
Phone 913-555-0147
Facebook: Lorabelle Quinn Blossoms
Instagram: @LorabelleQuinnBlossoms
Website: LorabelleQuinnBlossoms.example
Target Market(s)
Wholesale to Florists and Direct to Consumer via Farmers Market
Industry/Entity Type
Florist, Farm
Contact Information for Business Card
Name, Contact Info, Logo
Look and feel

```html
<!DOCTYPE html>
<html lang="en">
<head>
<meta charset="utf-8">
<title>Lorabelle Quinn Blossoms – Business Card</title>
<link rel="stylesheet" href="https://fonts.googleapis.com/css2?family=Open+Sans:wght@300;400;600;700&display=swap">
<style>
  :root {
    --forest: #0f2a30;
    --paper: #ffffff;
    --backdrop: #e9eaea;
    --ink-light: #ffffff;
  }
  * { box-sizing: border-box; margin: 0; padding: 0; }
  html, body {
    width: 1200px; height: 1200px; overflow: hidden;
    background: var(--backdrop);
    font-family: "Open Sans", Arial, sans-serif;
  }
  .card {
    position: absolute;
    left: 152px;
    width: 893px;
    height: 521px;
  }
  .card--front { top: 54px; background: var(--forest); color: var(--ink-light); }
  .card--back { top: 615px; background: var(--paper); border: 1px solid #d6d8d8; }

  .brand-name {
    position: absolute;
    left: 90px; top: 150px;
    width: 240px; height: 250px;
    display: flex; align-items: center; justify-content: center;
    text-align: center;
    font-size: 34px; font-weight: 600; line-height: 1.2;
    color: var(--ink-light);
  }
  .divider {
    position: absolute;
    left: 381px; top: 112px;
    width: 2px; height: 296px;
    background: var(--ink-light);
  }
  .person {
    position: absolute; left: 424px; top: 128px;
  }
  .person__name {
    font-size: 29px; font-weight: 600; letter-spacing: 0.5px; line-height: 1.2;
    text-transform: uppercase;
  }
  .person__role {
    margin-top: 6px; font-size: 21px; font-weight: 300;
  }
  .contact-list {
    position: absolute; left: 424px; top: 240px;
    list-style: none;
  }
  .contact-list li {
    display: flex; align-items: center;
    height: 37.5px;
    font-size: 22px; font-weight: 300;
  }
  .contact-list li.contact--web { font-weight: 600; }
  .contact-icon {
    width: 18px; height: 18px; margin-right: 22px; flex: none;
    display: flex; align-items: center; justify-content: center;
  }
  .contact-icon svg { width: 18px; height: 18px; }
  .dot-circle { width: 10px; height: 10px; border-radius: 50%; background: var(--ink-light); }
  .dot-square { width: 12px; height: 12px; border: 2px solid var(--ink-light); }

  .seal {
    position: absolute;
    left: 312px; top: 126px;
    width: 268px; height: 268px;
    border: 1.5px solid var(--forest);
    border-radius: 50%;
    display: flex; align-items: center; justify-content: center;
    text-align: center;
    font-size: 28px; font-weight: 600; line-height: 1.25;
    color: var(--forest);
  }
</style>
</head>
<body>

<section class="card card--front" aria-label="Business card front">
  <div class="brand-name">Lorabelle<br>Quinn<br>Blossoms</div>
  <div class="divider"></div>
  <div class="person">
    <h1 class="person__name">Darla Hoffstrom</h1>
    <p class="person__role">Owner</p>
  </div>
  <ul class="contact-list">
    <li>
      <span class="contact-icon">
        <svg viewBox="0 0 24 24" aria-hidden="true"><path fill="#fff" d="M6.6 10.8a15.1 15.1 0 0 0 6.6 6.6l2.2-2.2c.3-.3.7-.4 1-.2 1.1.4 2.3.6 3.6.6.6 0 1 .4 1 1V20c0 .6-.4 1-1 1A17 17 0 0 1 3 4c0-.6.4-1 1-1h3.5c.6 0 1 .4 1 1 0 1.3.2 2.5.6 3.6.1.3 0 .7-.2 1z"/></svg>
      </span>913-555-0147
    </li>
    <li><span class="contact-icon"><span class="dot-circle"></span></span>Lorabelle Quinn Blossoms</li>
    <li><span class="contact-icon"><span class="dot-square"></span></span>@LorabelleQuinnBlossoms</li>
    <li class="contact--web">
      <span class="contact-icon">
        <svg viewBox="0 0 24 24" aria-hidden="true" fill="none" stroke="#fff" stroke-width="1.8"><circle cx="12" cy="12" r="9"/><ellipse cx="12" cy="12" rx="4" ry="9"/><path d="M3 12h18M5 7h14M5 17h14"/></svg>
      </span>LorabelleQuinnBlossoms.example
    </li>
  </ul>
</section>

<section class="card card--back" aria-label="Business card back">
  <div class="seal">Lorabelle<br>Quinn<br>Blossoms</div>
</section>

</body>
</html>
```